Jewelry store needs fully functional Ecommerce website

Web Design Brief for our E-commerce Jewelry retail store.
Description

We need a fully coded Shopify website. The Shopify site will need to be fully functional with an Ecommerce integration (fully integrated with Paylo and All other gateways) and will need to be SEO optimized.
We sell jewelry items like: rings, earrings, necklaces etc. The website should have an elegant, modern, professional, fun, look.

***We would like the website to look and function similarly to this website:
https://velvorisco.com

Color Preference
Colors to be used are white background with black font and light pink/ purple/ gold tints. We have attached our logo as reference.

Functionalities
The store will function like a typical Ecommerce jewelry store, using the products/categories as the starting page. Going into individual product pages by selecting images and leading to a detailed “buy now” page for the selected product.

Target Market
Jewelry lovers.

Should Not Have:
- - Dull and common design
- - Messy/unstructured navigation

Coded - Design and coding required
Target Audience are women from 16-50 years old.
We will need to be able to add products and make modifications to the website as needed.

We need the following apps installed and Operating:
-Tally Shift; Order Look Up (rename “track your order”) ; Help Center (Questions and Answers) ; Pemmo Reviews; TXT Nudge; Drenoza Email Marketing ; Plivet (Chirpa messenger bump) ; Vantro multi- currency (translate currency to buyer) ; Discounted Upsell ; Easy Contact form App
We will need all products imported: (below is information for importing products). We will provide all links that serve entire active item product catalog in shopifys import format:
DataFeed:

If you are getting started with Shopify, a combination of the Shopify Import Format and XML feeds is ideal. The Shopify Import Format will output a file that can be uploaded into Shopify’s product database. After you import, you can use the XML feed and a third party app to keep the inventory up to date in real time, take down items that go out of stock etc., all without regular human intervention. There a several Shopify apps that can do this type of feed integration. We have had a good experience with Tally Shift, which is an app that can be configured to accept our XML feed and update products on a set schedule. You can even set your own margins based on our wholesale price with this app.

Shopify Formatted HTML TableTo make it easier to get started on Shopify, we included a format that outputs the required fields for a product import in Shopify. In order to use the embedded Excel file, first open the file (Auto-Shopify-Datasheet-Format.xslx), Refresh it (under Data tab), and then Save As with a new file name in a CSV (UTF-8) file. That file can then be split into smaller CSV files (if there is a limit on the number of products per file) for import into Shopify.

Target Market(s)

Jewelry Lovers

Industry/Entity Type

Jewelry Store

Coding

Number of Pages Required

5+ page

Colors
eda3c7
d3a5cc
ffffff

Requirements
Must have
• Color Preference
Colors to be used are white background with black font and light pink/ purple/ gold tints.

https://velvorisco.com
Should not have
• Should Not Have:

```html
<!DOCTYPE html>
<html lang="en">
<head>
<meta charset="utf-8">
<title>Amorine Lune — Fine Jewelry</title>
<link rel="stylesheet" href="https://fonts.googleapis.com/css2?family=Poppins:wght@300;400;500;600;700&family=Open+Sans:wght@400;600&display=swap">
<style>
:root{
  --pink:#e88fc2;
  --pink-soft:#eda3c7;
  --lilac:#d3a5cc;
  --ink:#1d1d1d;
  --text:#333;
  --muted:#777;
  --band:#e6e6e6;
  --card:#ececec;
  --white:#fff;
  --footer:#2a2a2a;
  --footer-text:#cfcfcf;
}
*{box-sizing:border-box;margin:0;padding:0}
html,body{width:1200px;height:3849px;overflow:hidden}
body{position:relative;background:var(--white);font-family:"Open Sans",sans-serif;color:var(--text)}
.abs{position:absolute}
h1,h2,h3{font-family:"Poppins",sans-serif;color:var(--ink)}
.btn{position:absolute;background:var(--pink);color:var(--ink);font-family:"Poppins",sans-serif;font-weight:600;font-size:16px;display:flex;align-items:center;justify-content:center;text-transform:uppercase}

/* header */
.site-header{top:0;left:0;width:1200px;height:163px;background:var(--white)}
.brand{left:143px;top:44px;display:flex;align-items:center;gap:14px}
.brand-dot{width:54px;height:54px;border-radius:50%;background:var(--lilac)}
.brand-name{font-family:"Poppins",sans-serif;font-size:30px;font-weight:400;color:#b07a78;line-height:1}
.brand-sub{font-size:10px;letter-spacing:3px;color:#b07a78;margin-top:6px;font-family:"Poppins",sans-serif}
.utility{top:44px;right:143px;display:flex;gap:40px}
.utility svg{width:30px;height:30px;stroke:#555;fill:none;stroke-width:1.6}
.main-nav{top:106px;right:145px;display:flex;gap:34px;font-family:"Poppins",sans-serif;font-size:14px;color:#333}
.main-nav .active{color:var(--pink)}

/* hero */
.hero{top:163px;left:0;width:1200px;height:496px;background:linear-gradient(90deg,#b9b4b3 0%,#8e8a8c 35%,#5d595e 55%,#555158 100%)}
.hero-title{right:145px;top:322px;text-align:right;color:#fff;font-size:49px;font-weight:700;line-height:64px;font-family:"Poppins",sans-serif}
.arrow svg{width:30px;height:40px;fill:none;stroke-width:4;stroke-linecap:round;stroke-linejoin:round}

/* welcome */
.welcome-title{left:143px;top:738px;font-size:40px;font-weight:700;line-height:48px}
.welcome-copy{left:143px;top:841px;width:440px;font-size:13px;line-height:29px;color:#333}
.photo{background:linear-gradient(135deg,#3a3a3a,#151515)}

/* bands */
.band{left:0;width:1200px;background:var(--band)}
.section-title{left:0;width:1200px;text-align:center;font-size:40px;font-weight:700}

.feature-card{top:1334px;width:297px;height:296px;background:var(--white);box-shadow:0 2px 6px rgba(0,0,0,.08)}
.feature-card .thumb{position:absolute;left:48px;top:50px;width:200px;height:150px;background:radial-gradient(circle,#d8d8de 0%,#f4f4f6 70%)}
.card-label{position:absolute;left:0;width:100%;text-align:center;font-family:"Poppins",sans-serif;color:var(--ink)}
.feature-card .card-label{top:238px;font-size:20px}

.latest-card{top:1869px;width:218px;height:217px;background:var(--card)}
.latest-card .thumb{position:absolute;left:34px;top:14px;width:150px;height:130px;background:radial-gradient(circle,#cfcfd4 0%,#ececec 72%)}
.latest-card .card-label{top:176px;font-size:17px}

/* reviews */
.review-tag{left:0;width:1200px;top:2325px;text-align:center;font-family:"Poppins",sans-serif;font-size:33px;font-weight:300;color:var(--ink)}
.review-text{left:150px;width:900px;top:2384px;text-align:center;font-family:"Poppins",sans-serif;font-size:21px;line-height:39px;color:#333}
.reviewer{left:0;width:1200px;top:2478px;text-align:center;font-family:"Poppins",sans-serif;font-weight:600;font-size:24px;color:var(--pink)}
.stars{left:545px;top:2520px;display:flex;gap:4px}
.stars svg{width:19px;height:19px;fill:var(--pink)}

/* blog */
.blog-title{left:626px;top:2783px;font-size:40px;font-weight:700}
.blog-lead{left:626px;top:2838px;width:460px;font-family:"Poppins",sans-serif;font-size:21px;line-height:32px;color:var(--ink)}
.blog-date{left:626px;top:2916px;font-family:"Poppins",sans-serif;font-size:16px;color:var(--pink)}
.blog-copy{left:626px;top:2950px;width:440px;font-size:13px;line-height:29px}

/* newsletter */
.news-title{left:0;width:1200px;top:3322px;text-align:center;font-size:43px;font-weight:600}
.news-sub{left:0;width:1200px;top:3391px;text-align:center;font-family:"Poppins",sans-serif;font-size:17px;color:var(--ink)}
.news-input{left:318px;top:3433px;width:436px;height:48px;background:#fff;padding-left:22px;display:flex;align-items:center;font-family:"Poppins",sans-serif;font-size:15px;color:#999}

/* footer */
.site-footer{left:0;top:3569px;width:1200px;height:280px;background:var(--footer);color:var(--footer-text)}
.foot-brand{left:143px;top:40px;display:flex;align-items:center;gap:10px;font-family:"Poppins",sans-serif;font-size:19px;color:#cfcfcf}
.foot-brand span{width:30px;height:30px;border-radius:50%;background:#d9d9d9}
.foot-copy{left:145px;top:116px;font-size:11px;line-height:27px}
.social{top:183px;width:43px;height:43px;border:1.5px solid #ccc;border-radius:50%;display:flex;align-items:center;justify-content:center;font-family:"Poppins",sans-serif;font-size:13px;color:#ddd}
.foot-col h3{font-family:"Poppins",sans-serif;font-weight:400;font-size:22px;color:#e6e6e6;margin-bottom:12px}
.foot-col ul{list-style:none;font-size:11px;line-height:27px}
.pay{top:95px;width:32px;height:20px;background:#f2f2f2;border-radius:2px;color:#333;font-family:"Poppins",sans-serif;font-size:7px;font-weight:600;display:flex;align-items:center;justify-content:center}
</style>
</head>
<body>

<header class="abs site-header">
  <div class="abs brand">
    <div class="brand-dot"></div>
    <div>
      <div class="brand-name">Amorine Lune</div>
      <div class="brand-sub">BY MARA AND LISE</div>
    </div>
  </div>
  <div class="abs utility">
    <svg viewBox="0 0 30 30"><circle cx="12" cy="12" r="9"/><line x1="19" y1="19" x2="28" y2="28"/></svg>
    <svg viewBox="0 0 30 30"><circle cx="15" cy="10" r="7"/><path d="M3 29c1-8 6-11 12-11s11 3 12 11z"/></svg>
    <svg viewBox="0 0 30 30"><path d="M15 27 4 16C-1 10 4 2 10 5c3 1 4 3 5 5 1-2 2-4 5-5 6-3 11 5 6 11z"/></svg>
    <svg viewBox="0 0 30 30"><rect x="4" y="8" width="22" height="20"/><path d="M10 8V5a5 5 0 0 1 10 0v3M11 13a4 4 0 0 0 8 0"/></svg>
  </div>
  <nav class="abs main-nav">
    <span class="active">PRODUCTS</span><span>SPECIALS</span><span>REVIEWS</span><span>ABOUT</span><span>CONTACT</span>
  </nav>
</header>

<section class="abs hero" role="img" aria-label="Photo of a woman wearing a heart pendant necklace against soft violet moon shapes"></section>
<div class="abs arrow" style="left:52px;top:392px"><svg viewBox="0 0 30 40" stroke="#fff"><path d="M22 6 8 20l14 14"/></svg></div>
<div class="abs arrow" style="left:1118px;top:392px"><svg viewBox="0 0 30 40" stroke="#fff"><path d="M8 6l14 14L8 34"/></svg></div>
<h1 class="abs hero-title">FUSCE EGET NEQUE<br>FAUCIBUS URNA</h1>
<div class="btn" style="left:919px;top:459px;width:136px;height:46px;font-size:20px">BUY NOW</div>

<h2 class="abs welcome-title">WELCOME TO<br>AMORINE LUNE</h2>
<p class="abs welcome-copy">Vestibulum condimentum, risus ut posuere cursus, velit justo accumsan sem, lobortis aliquet metus dui eu libero. Pellentesque a imperdiet dolor, et auctor est. Fusce sollicitudin lorem et luctus volutpat. Proin placerat dapibus gravida. In tristique tristique nulla eget hendrerit. Maecenas vel tortor accumsan quam varius imperdiet vel eget elit. Aenean facilisis tincidunt lectus, id dictum nisi luctus eget. Vivamus efficitur ex condimentum, malesuada eros.</p>
<div class="btn" style="left:143px;top:1056px;width:129px;height:48px">READ MORE</div>
<div class="abs photo" style="left:656px;top:747px;width:400px;height:357px" role="img" aria-label="Photo of a diamond ring resting on dark coal"></div>

<section class="abs band" style="top:1185px;height:536px"></section>
<h2 class="abs section-title" style="top:1258px">FEATURED PRODUCTS</h2>
<div class="abs feature-card" style="left:143px"><div class="thumb" role="img" aria-label="Photo of pearl drop earrings"></div><div class="card-label">Etiam mattis augue</div></div>
<div class="abs feature-card" style="left:451px"><div class="thumb" role="img" aria-label="Photo of a diamond ring set"></div><div class="card-label">Nulla facilisi</div></div>
<div class="abs feature-card" style="left:759px"><div class="thumb" role="img" aria-label="Photo of a heart charm bracelet"></div><div class="card-label">Cras sollicitudin</div></div>

<h2 class="abs section-title" style="top:1796px">LATEST PRODUCTS</h2>
<div class="abs arrow" style="left:52px;top:1958px"><svg viewBox="0 0 30 40" stroke="#999"><path d="M20 8 8 20l12 12"/></svg></div>
<div class="abs arrow" style="left:1118px;top:1958px"><svg viewBox="0 0 30 40" stroke="#999"><path d="M10 8l12 12-12 12"/></svg></div>
<div class="abs latest-card" style="left:143px"><div class="thumb" role="img" aria-label="Photo of a cushion cut ring"></div><div class="card-label">Aliquam erat</div></div>
<div class="abs latest-card" style="left:375px"><div class="thumb" role="img" aria-label="Photo of a solitaire pendant necklace"></div><div class="card-label">Quisque aliquet</div></div>
<div class="abs latest-card" style="left:607px"><div class="thumb" role="img" aria-label="Photo of a halo diamond ring"></div><div class="card-label">Pellentesque</div></div>
<div class="abs latest-card" style="left:839px"><div class="thumb" role="img" aria-label="Photo of a pearl bracelet"></div><div class="card-label">Vivamus eleifen</div></div>

<section class="abs band" style="top:2175px;height:529px"></section>
<h2 class="abs section-title" style="top:2250px">REVIEWS</h2>
<div class="abs review-tag">#Amorine Lune</div>
<p class="abs review-text">Vestibulum condimentum, risus ut posuere cursus, velit justo accumsan sem, lobortis aliquet metus dui eu libero. Pellentesque a imperdiet dolor, et auctor est.</p>
<div class="abs reviewer">Emily</div>
<div class="abs stars">
  <svg viewBox="0 0 20 20"><path d="M10 1l2.6 6 6.4.5-4.9 4.2 1.5 6.3L10 14.6 4.4 18l1.5-6.3L1 7.5 7.4 7z"/></svg>
  <svg viewBox="0 0 20 20"><path d="M10 1l2.6 6 6.4.5-4.9 4.2 1.5 6.3L10 14.6 4.4 18l1.5-6.3L1 7.5 7.4 7z"/></svg>
  <svg viewBox="0 0 20 20"><path d="M10 1l2.6 6 6.4.5-4.9 4.2 1.5 6.3L10 14.6 4.4 18l1.5-6.3L1 7.5 7.4 7z"/></svg>
  <svg viewBox="0 0 20 20"><path d="M10 1l2.6 6 6.4.5-4.9 4.2 1.5 6.3L10 14.6 4.4 18l1.5-6.3L1 7.5 7.4 7z"/></svg>
  <svg viewBox="0 0 20 20"><path d="M10 1l2.6 6 6.4.5-4.9 4.2 1.5 6.3L10 14.6 4.4 18l1.5-6.3L1 7.5 7.4 7z"/></svg>
</div>
<div class="btn" style="left:536px;top:2570px;width:127px;height:46px">VIEW ALL</div>

<div class="abs" style="left:143px;top:2794px;width:401px;height:356px;background:linear-gradient(135deg,#f4f1ea,#d9d4c8)" role="img" aria-label="Photo of engagement rings resting on white rose petals"></div>
<h2 class="abs blog-title">BLOG</h2>
<p class="abs blog-lead">Etiam vel massa elementum, bibendum tellus venenatis, feugiat massa.</p>
<div class="abs blog-date">24 February, 2021</div>
<p class="abs blog-copy">Maecenas vel tortor accumsan quam varius imperdiet vel eget elit. Aenean facilisis tincidunt lectus, id dictum nisi luctus eget. Vivamus efficitur ex condimentum, malesuada eros eget, feugiat nibh. Sed tellus ex, imperdiet eget gravida sit amet, volutpat eget turpis. In nec ultricies est. Etiam mattis augue vehicula odio posuere, sit amet.</p>
<div class="btn" style="left:626px;top:3103px;width:129px;height:47px">READ MORE</div>

<section class="abs band" style="top:3246px;height:323px"></section>
<h2 class="abs news-title">Newsletter Signup</h2>
<p class="abs news-sub">Pellentesque convallis molestie enim sit amet efficitur&nbsp; imperdiet lectus</p>
<div class="abs news-input">Email Address</div>
<div class="btn" style="left:754px;top:3433px;width:128px;height:48px">READ MORE</div>

<footer class="abs site-footer">
  <div class="abs foot-brand"><span></span>Amorine Lune</div>
  <p class="abs foot-copy">Copyright &copy; 2021&nbsp; Amorine Lune.<br>All rights reserved.</p>
  <div class="abs social" style="left:145px">Ch</div>
  <div class="abs social" style="left:202px">Ph</div>
  <div class="abs social" style="left:257px">Vi</div>
  <div class="abs foot-col" style="left:403px;top:34px"><h3>Links</h3><ul><li>Home</li><li>Products</li><li>Specials</li><li>Reviews</li><li>About</li><li>Contact</li></ul></div>
  <div class="abs foot-col" style="left:580px;top:34px"><h3>MyAccount</h3><ul><li>My Cart</li><li>Wishlist</li><li>Checkout</li><li>Shipping</li><li>Returns</li><li>FAQs</li></ul></div>
  <div class="abs foot-col" style="left:790px;top:34px"><h3>Payments</h3></div>
  <div class="abs pay" style="left:792px">Paylo</div>
  <div class="abs pay" style="left:847px">Cirqa</div>
  <div class="abs pay" style="left:904px">Vexa</div>
  <div class="abs pay" style="left:958px">Disqa</div>
  <div class="abs pay" style="left:1023px">Orvan</div>
</footer>

</body>
</html>
```